The Pebble Finch Leaflet. A5 2-sided Flyer for a UK Lawn Treatment Company

I need an A5 two-side leaflet / flyer designed for my Lawn Treatment company. The leaflet will be for door-drops so quick impact needed. Full colour, both sides. I provide lawn treatments to customers in the Exeter area of Devon. I would like to design to be clear, fresh and reflect the joy a good lawn and garden can bring.

Target Market(s)

Home Owners. 30-80 Years. Familys

Font styles to use
Sans Serif

Colors
9bcb3c
f78f20
ec1f27
33a6d7

Requirements
Must have
• Good front page picture
• Logo
• Contact details on front.
• Call to Action
• More details in Text file included in design.
Nice to have
• Clipart of a family / lady enjoying a lawn.

```html
<!DOCTYPE html>
<html lang="en">
<head>
<meta charset="utf-8">
<title>The Pebble Finch – A5 Leaflet</title>
<link rel="stylesheet" href="https://fonts.googleapis.com/css2?family=Roboto+Slab:wght@400;700&family=Roboto:wght@400;500;700&display=swap">
<style>
  :root{
    --page-bg:#e9eae6;
    --green:#2a8a1f;
    --green-dark:#1d6e17;
    --lime:#9bcb3c;
    --brown:#5e2a12;
    --brown-mid:#6b3217;
    --sky:#b9d7f2;
    --navy:#16324a;
    --red:#c8231e;
    --orange:#f78f20;
    --text:#2b2b2b;
    --white:#ffffff;
  }
  *{box-sizing:border-box;margin:0;padding:0}
  html,body{width:1200px;height:1000px;overflow:hidden}
  body{background:var(--page-bg);position:relative;font-family:"Roboto",Arial,sans-serif;color:var(--text)}
  .sheet{position:absolute;top:182px;width:450px;height:636px;background:var(--white);overflow:hidden;box-shadow:0 6px 18px rgba(0,0,0,.18)}
  .sheet--front{left:110px}
  .sheet--back{left:640px}

  /* ---------- front ---------- */
  .front-photo{position:absolute;left:0;top:0;width:450px;height:520px;
    background:linear-gradient(180deg,#f4f6f4 0%,#dfe6de 16%,#7f9b67 30%,#4f7a34 44%,#3f7f22 54%,#5ea52c 66%,#69b132 100%)}
  .front-fog{position:absolute;left:0;top:0;width:450px;height:150px;background:linear-gradient(180deg,rgba(255,255,255,.95),rgba(255,255,255,0))}
  .brand{position:absolute;left:26px;top:30px;display:flex;align-items:center;gap:16px}
  .brand__dot{width:64px;height:64px;border-radius:50%;background:var(--lime)}
  .brand__name{font-family:"Roboto Slab",Georgia,serif;font-weight:700;color:var(--green);font-size:26px;line-height:1.05;text-align:center;border-top:2px solid var(--green);border-bottom:2px solid var(--green);padding:4px 6px}
  .badge{position:absolute;left:322px;top:362px;width:112px;height:112px;border-radius:50%;background:var(--navy);border:12px solid #7fb23a;box-shadow:0 0 0 3px #e9f1dd}
  .front-curves{position:absolute;left:0;top:380px}
  .front-copy{position:absolute;left:0;top:520px;width:450px;text-align:center}
  .front-copy__headline{font-family:"Roboto Slab",Georgia,serif;font-weight:700;color:var(--green);font-size:26px;line-height:1;letter-spacing:.2px}
  .front-copy__sub{font-family:"Roboto Slab",Georgia,serif;font-weight:700;color:var(--navy);font-size:17px;line-height:1.15;margin-top:2px}
  .front-copy__call{font-family:"Roboto",Arial,sans-serif;color:var(--navy);font-size:12.5px;margin-top:4px;line-height:1.2}
  .front-copy__call .num{color:var(--green)}
  .web-band{position:absolute;left:0;top:606px;width:450px;height:22px;background:var(--green);color:var(--white);font-size:13px;text-align:center;line-height:22px}
  .web-band .hl{color:#ffd84a}

  /* ---------- back ---------- */
  .back-photo{position:absolute;left:0;top:0;width:450px;height:250px;
    background:linear-gradient(180deg,#3b5e28 0%,#5f8a3a 35%,#6fae32 60%,#7fc03c 100%)}
  .back-curves{position:absolute;left:0;top:140px}
  .photo-circle{position:absolute;border-radius:50%;border:4px solid var(--green)}
  .photo-circle--family{left:40px;top:160px;width:124px;height:124px;background:linear-gradient(180deg,#a7c46a,#6aa83a 60%,#4d8b25)}
  .photo-circle--lawn{left:340px;top:128px;width:114px;height:114px;background:linear-gradient(180deg,#2f5a20,#5b9a2c 55%,#76b735)}
  .col{position:absolute;font-size:9.2px;line-height:1.32}
  .col--left{left:22px;top:290px;width:208px}
  .col--right{left:242px;top:262px;width:196px}
  .sec-title{font-family:"Roboto",Arial,sans-serif;font-weight:700;color:var(--brown);font-size:9.6px;margin:0 0 2px;display:flex;align-items:center;gap:4px}
  .sec-title::before{content:"";width:5px;height:5px;background:var(--green)}
  .sec-title--plain::before{display:none}
  .col p{margin-bottom:9px;text-align:justify}
  .cta-line{color:var(--green);font-weight:500}
  .service-list{list-style:none;margin-top:4px}
  .service-list li{font-family:"Roboto Slab",Georgia,serif;color:var(--green);font-size:10px;display:flex;align-items:center;gap:5px;margin-bottom:2px}
  .service-list svg{flex:none}
  .testimonials{position:absolute;left:250px;top:474px;width:188px;height:104px;background:var(--brown-mid);border-radius:10px;color:var(--white);font-size:8.4px;line-height:1.3;padding:18px 10px 8px;font-style:italic}
  .testimonials__tab{position:absolute;left:10px;top:-8px;background:var(--green);color:var(--white);font-style:normal;font-size:10px;padding:2px 10px;border-radius:5px}
  .testimonials p{margin-bottom:6px}
  .testimonials .who{color:var(--orange)}
  .grass-strip{position:absolute;left:0;top:574px;width:450px;height:62px;background:linear-gradient(180deg,#ffffff 0%,#d8ecc0 35%,#7fbf3a 70%,#4f9a22 100%)}
  .strapline{position:absolute;left:20px;top:586px;font-family:"Roboto Slab",Georgia,serif;font-weight:700;color:var(--red);font-size:13px;line-height:1}
  .back-brand{position:absolute;left:232px;top:584px;width:110px;display:flex;flex-direction:column;align-items:center;gap:3px}
  .back-brand__dot{width:20px;height:20px;border-radius:50%;background:var(--lime)}
  .back-brand__name{font-family:"Roboto Slab",Georgia,serif;font-weight:700;color:var(--green);font-size:9.5px;white-space:nowrap;border-top:1px solid var(--green);border-bottom:1px solid var(--green);padding:1px 2px}
  .back-call{position:absolute;left:352px;top:588px;font-family:"Roboto Slab",Georgia,serif;font-weight:700;color:var(--green-dark);font-size:11.5px;line-height:1.1;white-space:nowrap}
</style>
</head>
<body>

<section class="sheet sheet--front" aria-label="Leaflet front">
  <div class="front-photo" role="img" aria-label="Photograph of a lush green lawn edged by flowering shrubs in morning mist"></div>
  <div class="front-fog"></div>
  <div class="brand">
    <span class="brand__dot"></span>
    <span class="brand__name">THE PEBBLE FINCH</span>
  </div>
  <div class="badge" aria-hidden="true"></div>
  <svg class="front-curves" width="450" height="256" viewBox="0 0 450 256" aria-hidden="true">
    <path d="M0 118 C90 50 230 48 330 58 C390 64 430 30 450 0 L450 256 L0 256Z" fill="var(--brown)"/>
    <path d="M0 138 C90 74 230 68 330 78 C395 84 435 55 450 25 L450 256 L0 256Z" fill="var(--sky)"/>
    <path d="M22 132 C80 104 160 88 260 88 C170 96 92 112 22 132Z" fill="var(--green)"/>
    <path d="M46 130 C110 106 190 96 260 92 C185 102 116 114 46 130Z" fill="var(--lime)"/>
  </svg>
  <div class="front-copy">
    <div class="front-copy__headline">TREATMENTS AND ADVICE</div>
    <div class="front-copy__sub">TO KEEP YOUR LAWN LOOKING NICE</div>
    <div class="front-copy__call">CALL TODAY ON <span class="num">01632 960418</span> OR TEXT <span class="num">07700 900317</span><br>BOOK YOUR LAWN SURVEY</div>
  </div>
  <div class="web-band">www.<span class="hl">pebblefinch</span>.co.uk</div>
</section>

<section class="sheet sheet--back" aria-label="Leaflet back">
  <div class="back-photo" role="img" aria-label="Photograph of a striped garden lawn with hedges, conifers and potted plants"></div>
  <svg class="back-curves" width="450" height="140" viewBox="0 0 450 140" aria-hidden="true">
    <path d="M0 110 C120 70 280 90 380 70 C420 62 440 40 450 20 L450 140 L0 140Z" fill="var(--green)"/>
    <path d="M0 122 C120 90 280 104 380 86 C420 78 440 60 450 44 L450 140 L0 140Z" fill="var(--white)"/>
  </svg>
  <div class="photo-circle photo-circle--family" role="img" aria-label="Photograph of a family relaxing together on a lawn"></div>
  <div class="photo-circle photo-circle--lawn" role="img" aria-label="Photograph of a neat garden lawn with shrubs"></div>

  <div class="col col--left">
    <h3 class="sec-title">FOR A BEAUTIFUL WEED-FREE LAWN</h3>
    <p>Call The Pebble Finch today and start your journey to a wonderful, lush, green lawn you and your family can enjoy. Arrange a no-obligation lawn survey and quotation at a time to suit you.<br><span class="cta-line">Call 01632 960418 now.</span></p>
    <h3 class="sec-title">I WILL UNDERSTAND YOUR LAWN</h3>
    <p>Every lawn is unique. I take time to gain a comprehensive understanding of your lawn and its situation. I will also listen to you and understand your problems and your aspirations for your grass.</p>
    <h3 class="sec-title">YOUR LAWN TREATMENTS</h3>
    <p>I will create a custom treatment programme tailored to your lawn. I may also recommend some remedial treatments to correct any existing problems. There is no contract to sign. I guarantee all treatments.</p>
  </div>

  <div class="col col--right">
    <h3 class="sec-title sec-title--plain">INDUSTRY-LEADING LAWN CARE</h3>
    <p>I have 8 years of experience in the leading edge of domestic lawn care. I have a comprehensive range of treatments including:</p>
    <ul class="service-list">
      <li><svg width="9" height="9" viewBox="0 0 10 10"><circle cx="5" cy="5" r="4.3" fill="none" stroke="#2a8a1f"/><path d="M3 5.2 4.5 6.6 7.2 3.6" fill="none" stroke="#2a8a1f" stroke-width="1.2"/></svg>SCARIFICATION</li>
      <li><svg width="9" height="9" viewBox="0 0 10 10"><circle cx="5" cy="5" r="4.3" fill="none" stroke="#2a8a1f"/><path d="M3 5.2 4.5 6.6 7.2 3.6" fill="none" stroke="#2a8a1f" stroke-width="1.2"/></svg>AERATION</li>
      <li><svg width="9" height="9" viewBox="0 0 10 10"><circle cx="5" cy="5" r="4.3" fill="none" stroke="#2a8a1f"/><path d="M3 5.2 4.5 6.6 7.2 3.6" fill="none" stroke="#2a8a1f" stroke-width="1.2"/></svg>MOSS CONTROL</li>
      <li><svg width="9" height="9" viewBox="0 0 10 10"><circle cx="5" cy="5" r="4.3" fill="none" stroke="#2a8a1f"/><path d="M3 5.2 4.5 6.6 7.2 3.6" fill="none" stroke="#2a8a1f" stroke-width="1.2"/></svg>OVERSEEDING</li>
      <li><svg width="9" height="9" viewBox="0 0 10 10"><circle cx="5" cy="5" r="4.3" fill="none" stroke="#2a8a1f"/><path d="M3 5.2 4.5 6.6 7.2 3.6" fill="none" stroke="#2a8a1f" stroke-width="1.2"/></svg>TOP DRESSING</li>
      <li><svg width="9" height="9" viewBox="0 0 10 10"><circle cx="5" cy="5" r="4.3" fill="none" stroke="#2a8a1f"/><path d="M3 5.2 4.5 6.6 7.2 3.6" fill="none" stroke="#2a8a1f" stroke-width="1.2"/></svg>LAWN REPAIRS</li>
      <li><svg width="9" height="9" viewBox="0 0 10 10"><circle cx="5" cy="5" r="4.3" fill="none" stroke="#2a8a1f"/><path d="M3 5.2 4.5 6.6 7.2 3.6" fill="none" stroke="#2a8a1f" stroke-width="1.2"/></svg>FERTILISATION &amp; WEED CONTROL</li>
      <li><svg width="9" height="9" viewBox="0 0 10 10"><circle cx="5" cy="5" r="4.3" fill="none" stroke="#2a8a1f"/><path d="M3 5.2 4.5 6.6 7.2 3.6" fill="none" stroke="#2a8a1f" stroke-width="1.2"/></svg>PEST AND DISEASE MANAGEMENT</li>
      <li><svg width="9" height="9" viewBox="0 0 10 10"><circle cx="5" cy="5" r="4.3" fill="none" stroke="#2a8a1f"/><path d="M3 5.2 4.5 6.6 7.2 3.6" fill="none" stroke="#2a8a1f" stroke-width="1.2"/></svg>SPECIAL EVENT PREPARATION</li>
    </ul>
  </div>

  <div class="testimonials">
    <span class="testimonials__tab">TESTIMONIALS</span>
    <p>"Thank you for keeping our lawn in great shape for so long, I've been really pleased with how it has looked since you took care of it." - <span class="who">Colin</span></p>
    <p>"My lawn has never looked better since the day that you started to look after it for me." - <span class="who">Mrs. Rowe</span></p>
  </div>

  <div class="grass-strip" role="img" aria-label="Close-up photograph of fresh green grass blades"></div>
  <div class="strapline">SAVE TIME AND MONEY<br>AND LEAVE YOUR<br>LAWN TO AN EXPERT.</div>
  <div class="back-brand">
    <span class="back-brand__dot"></span>
    <span class="back-brand__name">THE PEBBLE FINCH</span>
  </div>
  <div class="back-call">CALL<br>01632 960418<br>TODAY.</div>
</section>

</body>
</html>
```